quickpine website

I need the graphics and images created for a web site. I have settled on a layout but are open to alternatives

I have already purchased the images I want to use.

I want the graphics/design to really give the web site a lift without deviating from the core concept (which is lots of white space, clean looking)

I have further files to upload for use (another 4).

The link to the current web site that requires re-skinning is: http://www.tarvinmarketing.com.au/cgi-bin/xmlweb.cgi/scriptlet/quickpine?cms_section=quickpine&cms_name=home
Updates

I forgot to mention that I would the design elements of the various text boxes down the right hand side and along the bottom of the page to be improved.  At the moment they look very one dimensional and boring.

Thanks

All files have now been uploaded.

Hi Guys
Some great designs are coming through.  I thought I would share elements that I like for each for those of you who are prepared to tweek their submissions.

Design ID 27087
1. Used used the proper logo file supplied
2. Like the use of images and design of the various text boxes down the right hand side of the page
3.  I like the footer - but would maybe change some of the images used
4.  I like the navigation bar

Design ID 27265
1. Like the placement of icons up the top.  I think this concept would work if there were maybe three other icons up there as well

Design ID 27266
1.  Like the design elements of the various text boxes down the right hand side of the page
2.  Like the grey background strip down the right hand side of page

Key thing I would like improved:
1.  The style and use of text in the header/banner.  I also think it looks a little one dimensional

Thanks

Rgds
Dale

Target Market(s)

SME businesses

Number of Pages Required

1 page

Requirements
Must have
• 1. Header/Banner must replicate concept provided
2. Please check out this web site as it is the design inspiration and should heavily influence the final design (use of colour etc) - www.plovinstudio.com

```html
<!DOCTYPE html>
<html lang="en">
<head>
<meta charset="utf-8">
<title>quickpine marketing</title>
<link rel="stylesheet" href="https://fonts.googleapis.com/css2?family=Gelasio:wght@400;500&family=Arimo:wght@400;700&display=swap">
<style>
:root{
  --sky:#1fa6e6;
  --sky-deep:#2a73c9;
  --link:#1c5fb5;
  --heading:#1ca0e0;
  --orange:#f7a400;
  --ink:#222;
  --panel:#f2f8fc;
  --footer-blue:#0ba9ec;
  --footer-grey:#6b6b6b;
  --field:#f7fbfe;
  --field-line:#d5e2ea;
}
*{box-sizing:border-box;margin:0;padding:0}
html,body{width:904px;height:1200px;overflow:hidden;background:#fff}
body{position:relative;font-family:"Arimo",Arial,sans-serif;color:var(--ink)}
.abs{position:absolute}

/* header */
.brand{left:66px;top:10px;display:flex;align-items:center;gap:6px}
.brand-dot{width:44px;height:44px;border-radius:50%;background:var(--sky)}
.brand-name{font-family:"Arimo",Arial,sans-serif;font-size:30px;font-weight:400;color:var(--sky)}
.nav{left:358px;top:29px;display:flex;align-items:center;font-size:9.5px;color:#333}
.nav a{color:#333;text-decoration:none;margin-right:29px}
.nav .current{background:var(--orange);color:#fff;font-weight:700;padding:6px 13px;border-radius:12px;margin-right:19px}
.nav a:last-child{margin-right:0}

/* banner */
.banner{left:58px;top:82px;width:793px;height:239px;background:linear-gradient(100deg,#2e6fd2 0%,#3f8be0 45%,#8cc7f0 85%,#bfe1f7 100%)}
.banner-text{left:28px;top:26px;color:#fff;font-family:"Gelasio",Georgia,serif}
.banner h1{font-weight:400;font-size:45px;line-height:1.1}
.banner .lede{margin-top:16px;font-size:16px;line-height:24px}
.banner .call{margin-top:20px;font-size:22px}
.video{left:546px;top:24px;width:237px;height:193px;background:#111}
.video-still{left:0;top:33px;width:237px;height:160px;background:linear-gradient(90deg,#1c1c1c,#6d6d6d 55%,#2a2a2a)}
.video-avatar{left:9px;top:8px;width:40px;height:40px;background:#5cc3f0}
.video-title{left:55px;top:11px;background:#000;padding:1px 3px;font-weight:700;font-size:14px;color:var(--sky)}
.video-by{left:55px;top:34px;background:#000;padding:1px 3px;font-size:9px;color:#fff}
.video-by span{color:var(--sky)}
.video-controls{left:8px;top:159px;width:222px;height:28px;display:flex;align-items:center;gap:8px}
.play{width:48px;height:28px;background:#222;display:flex;align-items:center;justify-content:center}
.track{position:relative;width:96px;height:6px;border:1px solid #ddd}
.time{position:absolute;left:-2px;top:-18px;background:#fff;color:#000;font-size:7px;padding:1px 2px}
.vol{display:flex;gap:2px}
.vol i{width:2px;height:9px;background:#3ab0ec}

/* main */
.main{left:64px;top:343px;width:490px}
.main h2{font-weight:400;font-size:22px;color:var(--heading);margin-bottom:19px}
.main h3{font-weight:400;font-size:13px;color:var(--link);margin-bottom:10px}
.main p{font-size:9.3px;line-height:14.3px;margin-bottom:22px}
.services{left:64px;top:651px;width:490px}
.service{position:relative;height:100px}
.service-img{position:absolute;left:0;top:0;width:102px;height:67px}
.service-body{position:absolute;left:124px;top:0;width:360px}
.service-body h4{font-weight:400;font-size:11px;color:var(--link);margin-bottom:10px}
.service-body p{font-size:9px;line-height:14.3px;margin-bottom:9px}
.more{color:var(--orange);font-size:9px;font-weight:700;text-decoration:none}

/* sidebar */
.panel{left:604px;width:238px;background:var(--panel)}
.panel h5{font-family:"Gelasio",Georgia,serif;font-weight:400;font-size:15px;color:#222;letter-spacing:.3px}
.tag{position:absolute;left:14px;background:var(--orange);color:#fff;font-family:"Gelasio",Georgia,serif;font-size:11px;padding:2px 6px;transform:rotate(-8deg)}
.form-row{display:flex;align-items:center;font-size:8px;height:24px}
.form-row label{width:73px}
.field{width:116px;height:15px;background:var(--field);border:1px solid var(--field-line)}
.btn{display:inline-block;background:var(--sky);color:#fff;font-size:7.5px;font-weight:700;padding:4px 9px;border-radius:3px}
.list{list-style:none;margin-top:16px}
.list li{position:relative;padding-left:14px;font-size:8px;color:var(--sky);height:20.6px}
.list li::before{content:"";position:absolute;left:1px;top:2px;width:6px;height:6px;border-radius:50%;background:var(--sky)}

/* footer */
.footer{left:57px;top:1051px;width:793px;height:123px;background:var(--footer-blue);border-radius:6px 6px 0 0}
.promo{position:absolute;top:16px;width:190px}
.promo-icon{position:absolute;left:0;top:0;width:34px;height:34px;border-radius:50%}
.promo-text{margin-left:47px;color:#fff;font-size:8.6px;font-weight:700;letter-spacing:2px;line-height:11.5px}
.promo-text .learn{margin-top:12px;font-weight:400}
.promo-text .learn b{color:#0b4f86}
.bottom{left:57px;top:1174px;width:793px;height:26px;background:var(--footer-grey);color:#fff;font-size:7.5px;letter-spacing:1.2px;display:flex;align-items:center;justify-content:center}
</style>
</head>
<body>

<header>
  <div class="abs brand"><span class="brand-dot"></span><span class="brand-name">quickpine</span></div>
  <nav class="abs nav">
    <a class="current" href="#">HOME</a>
    <a href="#">WHAT WE’RE WORKING ON</a>
    <a href="#">ABOUT US</a>
    <a href="#">MEDIA</a>
    <a href="#">BLOG</a>
    <a href="#">CONTACT US</a>
  </nav>
</header>

<section class="abs banner" role="img" aria-label="Blue sky with soft white clouds">
  <div class="abs banner-text">
    <h1>Reshaping Business</h1>
    <p class="lede">quickpine is a marketing agency specialising<br>in marketing campaign design &amp; execution using<br>traditional and digital media</p>
    <p class="call">Call Now on 1300 482 615</p>
  </div>
  <div class="abs video">
    <div class="abs video-still" role="img" aria-label="Black and white video still of a presenter speaking"></div>
    <div class="abs video-avatar"></div>
    <div class="abs video-title">Quick Pine</div>
    <div class="abs video-by">from <span>Dale Renwick</span></div>
    <div class="abs video-controls">
      <div class="play"><svg width="14" height="14" viewBox="0 0 14 14"><path d="M2 1 L13 7 L2 13 Z" fill="#fff"/></svg></div>
      <div class="track"><span class="time">00:44</span></div>
      <div class="vol"><i></i><i></i><i></i><i></i><i></i><i></i><i></i></div>
      <svg width="10" height="10" viewBox="0 0 10 10"><path d="M0 0h3v1H1v2H0zM10 0H7v1h2v2h1zM0 10h3V9H1V7H0zM10 10H7V9h2V7h1z" fill="#fff"/></svg>
    </div>
  </div>
</section>

<main>
  <div class="abs main">
    <h2>Quickpine Marketing</h2>
    <h3>At quickpine marketing we’re reshaping business and building brands.</h3>
    <p>We’re helping businesses like yours build their customer base and penetrate new markets.&nbsp; Quickpine achieve this through strategic market campaign design and execution using a combination of traditional and digital media.</p>
    <h3>We’re your outsourced marketing department.</h3>
    <p>As your outsourced marketing managers, quickpine specialise in providing marketing strategies, brand &amp; logo development, public relations campaigns, advertising strategies, social media strategies, web site design and online marketing strategies.</p>
    <h3>We cause gravity to your business.</h3>
    <p>We’ll reposition your business in the marketplace so that it resonates with your target market.&nbsp; We’ll then help you implement powerful online and offline lead generation and sales strategies.</p>
  </div>

  <div class="abs services">
    <div class="service">
      <div class="service-img" role="img" aria-label="Two businessmen in suits discussing strategy" style="background:linear-gradient(135deg,#c9c2b6,#6b6358)"></div>
      <div class="service-body"><h4>Marketing &amp; PR Strategy</h4><p>Learn more about how we can help build your customer base and penetrate new markets.</p><a class="more" href="#">Find out more…</a></div>
    </div>
    <div class="service">
      <div class="service-img" role="img" aria-label="Darts hitting a target" style="background:linear-gradient(180deg,#ffffff,#e6e6e6)"></div>
      <div class="service-body"><h4>Campaign Design &amp; Execution</h4><p>Seeking a marketing plan that works?&nbsp; Learn more about how we implement our powerful marketing strategies.</p><a class="more" href="#">Find out more…</a></div>
    </div>
    <div class="service">
      <div class="service-img" role="img" aria-label="Head profile filled with colourful gears" style="background:radial-gradient(circle at 45% 45%,#e8e8e8,#ffffff 70%)"></div>
      <div class="service-body"><h4>Creative</h4><p>Quickpine design &amp; develop brochures, podcasts, vodcasts, advertisements,<br>e-marketing campaigns, direct marketing &amp; promotional videos</p><a class="more" href="#">Find out more…</a></div>
    </div>
    <div class="service">
      <div class="service-img" role="img" aria-label="Light bulb with an at sign filament" style="background:radial-gradient(circle at 50% 40%,#e4e4e4,#ffffff 65%)"></div>
      <div class="service-body"><h4>Web Site Design &amp; Online Strategy</h4><p>What is your web site saying about your business?&nbsp; Learn how quickpine can build a new web site for your business that generates enquiries and convert sales.</p><a class="more" href="#">Find out more…</a></div>
    </div>
  </div>
</main>

<aside>
  <section class="abs panel" style="top:340px;height:165px">
    <span class="tag" style="top:17px">FREE</span>
    <h5 class="abs" style="left:43px;top:27px">MARKETING ASSESSMENT</h5>
    <div class="abs" style="left:18px;top:58px">
      <div class="form-row"><label>Name:</label><span class="field"></span></div>
      <div class="form-row"><label>Company Name:</label><span class="field"></span></div>
      <div class="form-row"><label>Email:</label><span class="field"></span></div>
    </div>
    <span class="abs btn" style="left:106px;top:128px">Get Your Assessment</span>
  </section>

  <section class="abs panel" style="top:522px;height:140px">
    <span class="tag" style="top:22px">JOIN</span>
    <h5 class="abs" style="left:46px;top:32px">OUR MAILING LIST</h5>
    <div class="abs" style="left:18px;top:62px">
      <div class="form-row"><label style="width:71px">Name:</label><span class="field"></span></div>
      <div class="form-row"><label style="width:71px">Email:</label><span class="field"></span></div>
    </div>
    <span class="abs btn" style="left:153px;top:107px">Subscribe</span>
  </section>

  <section class="abs panel" style="top:681px;height:173px;padding:20px 13px">
    <h5>WHAT ARE YOU LOOKING FOR?</h5>
    <ul class="list">
      <li>I want to increase brand awareness</li>
      <li>I want greater lead generation</li>
      <li>I want a powerful online strategy</li>
      <li>I want to launch a new product or service</li>
      <li>I want a marketing overhaul</li>
    </ul>
  </section>

  <section class="abs panel" style="top:872px;height:145px;padding:20px 14px">
    <h5>RECENT MEDIA</h5>
    <ul class="list" style="margin-top:16px">
      <li>Podcast on 7 Ways to Improve your Marketing</li>
      <li>Article on Why Most Marketing Fails</li>
      <li>Podcast Interview with Mira Castell</li>
    </ul>
    <a class="more" href="#">More media items…</a>
  </section>
</aside>

<footer>
  <div class="abs footer">
    <div class="promo" style="left:8px">
      <div class="promo-icon" role="img" aria-label="Globe icon" style="background:linear-gradient(135deg,#d8ecfa,#2a73c9)"></div>
      <div class="promo-text">Want a Web solution that actually Builds Business?<div class="learn"><b>Learn more</b> about our Web Development &amp; online Marketing programs.</div></div>
    </div>
    <div class="promo" style="left:204px">
      <div class="promo-icon" role="img" aria-label="Television icon" style="border-radius:4px;background:linear-gradient(180deg,#555,#222)"></div>
      <div class="promo-text">Could a Video Presentation make all the Difference to Your Business?<div class="learn"><b>Learn more</b> about our Media Production solutions.</div></div>
    </div>
    <div class="promo" style="left:401px">
      <div class="promo-icon" role="img" aria-label="Business adviser icon" style="background:linear-gradient(180deg,#f3f3f3,#c33)"></div>
      <div class="promo-text">Feel Like You’re Not in Control of Your Business?<div class="learn"><b>Learn more</b> about our Business Advisory Programs.</div></div>
    </div>
    <div class="promo" style="left:598px">
      <div class="promo-icon" role="img" aria-label="Sales team icon" style="background:linear-gradient(180deg,#f3f3f3,#2a73c9)"></div>
      <div class="promo-text">Looking to Fine Tune Your Sales Team?<div class="learn"><b>Learn more</b> about our Sales Force Effectiveness programs.</div></div>
    </div>
  </div>
  <div class="abs bottom"><b>Sitemap</b>&nbsp;&nbsp;|&nbsp;&nbsp;© quickpine (02) 9418 3307 Location: Sydney, Australia</div>
</footer>

</body>
</html>
```